KW Sports & Remedial Massage needs a new logo & business card design

The design is for my Sports and remedial massage business. My business is aimed at everyone who has a muscle ache or injury so not just sports related. I need a design which is sharp, clear and professional. No greens, or pastel colours or floral/girly designs. Perhaps just a Navy background and white text or other way around or perhaps grey. I want to make it clear that I treat everyone and not just sporty people.

Target Market(s)

People with muscle aches or sports injuries

Industry/Entity Type

Health And Wellness

Contact Information for Business Card

It needs to also include the following:
Name: Marion Kebbell
Mobile No: 07432 519 268
Email: marionkebbell@postvane.com
Qualifications: Dip SM, Dip SRM

Logo Text

KW Sports & Remedial Massage

Font styles to use
Serif
Other font styles liked:
• Tahoma, Verdana

Colors
5c5c5c
7f7f7f
9d9d9d
0255a3
3176b5
85abd2

Requirements
Must have
• I was thinking of a few simple people figures at the bottom of the card to highlight this i.e. a gardener, musician mixed in with a cyclist and tennis player.
Should not have
• Anything which indicates beauty therapy or relaxing. I am there to get rid of aches and pains and often to give rehab to certain injuries.

```html
<!DOCTYPE html>
<html lang="en">
<head>
<meta charset="utf-8">
<title>KW Sports &amp; Remedial Massage – Business Card</title>
<link rel="stylesheet" href="https://fonts.googleapis.com/css2?family=Questrial&display=swap">
<style>
  :root {
    --page-bg: #e9eaec;
    --card-bg: #ffffff;
    --card-fade: #f1f2f4;
    --text-dark: #474747;
    --text-grey: #6f6f6f;
    --brand-blue: #2a6a9a;
    --band-navy: #225a87;
    --band-teal: #3a8fb2;
    --icon-blue: #2f6fa5;
  }
  * { margin: 0; padding: 0; box-sizing: border-box; }
  html, body {
    width: 1200px;
    height: 900px;
    overflow: hidden;
    background: var(--page-bg);
    font-family: "Questrial", "Century Gothic", sans-serif;
  }
  .business-card {
    position: absolute;
    left: 50px;
    top: 128px;
    width: 1100px;
    height: 644px;
    background: linear-gradient(180deg, var(--card-bg) 60%, var(--card-fade) 100%);
    overflow: hidden;
    box-shadow: 0 2px 10px rgba(0,0,0,0.12);
  }
  .footer-band {
    position: absolute;
    left: 0;
    bottom: 0;
    width: 100%;
    height: 120px;
    background: linear-gradient(90deg, var(--band-navy) 0%, var(--band-teal) 100%);
  }
  .brand-name {
    position: absolute;
    left: 0;
    width: 100%;
    top: 168px;
    text-align: center;
    color: var(--text-grey);
    font-weight: 400;
    line-height: 1;
  }
  .brand-name .brand-main {
    display: block;
    font-size: 50px;
    letter-spacing: 0.5px;
  }
  .brand-name .brand-sub {
    display: block;
    margin-top: 8px;
    font-size: 31px;
    letter-spacing: 0.5px;
  }
  .person {
    position: absolute;
    left: 60px;
    top: 338px;
    width: 440px;
    text-align: center;
  }
  .person-name {
    font-size: 58px;
    font-weight: 400;
    color: var(--text-dark);
    line-height: 1;
    letter-spacing: 0.5px;
  }
  .person-quals {
    margin-top: 14px;
    font-size: 34px;
    color: var(--brand-blue);
    line-height: 1;
  }
  .contact-list {
    position: absolute;
    left: 560px;
    top: 353px;
    list-style: none;
  }
  .contact-item {
    display: flex;
    align-items: center;
    height: 50px;
    font-size: 29px;
    color: var(--text-dark);
  }
  .contact-icon {
    width: 30px;
    height: 30px;
    margin-right: 14px;
    flex: none;
  }
</style>
</head>
<body>
  <main class="business-card">
    <div class="footer-band" role="img" aria-label="Decorative blue band along the bottom edge of the card"></div>

    <h1 class="brand-name">
      <span class="brand-main">KW Sports</span>
      <span class="brand-sub">&amp; Remedial Massage</span>
    </h1>

    <section class="person">
      <h2 class="person-name">Marion Kebbell</h2>
      <p class="person-quals">Dip SM, Dip SRM</p>
    </section>

    <ul class="contact-list">
      <li class="contact-item">
        <svg class="contact-icon" viewBox="0 0 30 30" aria-hidden="true">
          <rect x="9" y="3" width="12" height="24" rx="2" fill="none" stroke="var(--icon-blue)" stroke-width="2.4"/>
          <circle cx="15" cy="23" r="1.3" fill="var(--icon-blue)"/>
        </svg>
        <span>07432 519 268</span>
      </li>
      <li class="contact-item">
        <svg class="contact-icon" viewBox="0 0 30 30" aria-hidden="true">
          <rect x="2" y="8" width="26" height="16" fill="var(--icon-blue)"/>
          <path d="M2 8 L15 18 L28 8" fill="none" stroke="#ffffff" stroke-width="1.8"/>
          <path d="M2 24 L11 15 M28 24 L19 15" fill="none" stroke="#ffffff" stroke-width="1.4"/>
        </svg>
        <span>marionkebbell@postvane.com</span>
      </li>
    </ul>
  </main>
</body>
</html>
```